Heritage Hollow Business Cards

Require a business card design. <br/><br/>Needs to include logo (either round or long version) plus these details:<br/>Maya Torvel<br/>Heritage Hollow<br/>maya@quonbrook.com.au<br/>02 6481 7390<br/>PO Box Glenwarra NSW 2913<br/>www.heritagehollow.com.au<br/><br/>I need in an editable format so that I can create for multiple staff members. <br/><br/>

Target Market(s)

We are an online store selling renovation products to home owners are builders. Looking for a classic classy design.

Industry/Entity Type

Home And Garden

Contact Information for Business Card

Maya Torvel
Heritage Hollow
maya@quonbrook.com.au
02 6481 7390
PO Box Glenwarra NSW 2913
www.heritagehollow.com.au

Colors

Designer to choose colors to be used in the design.

Requirements
Must have
• Must include Logo.

```html
<!DOCTYPE html>
<html lang="en">
<head>
<meta charset="utf-8">
<title>Heritage Hollow Business Cards</title>
<link href="https://fonts.googleapis.com/css2?family=Noto+Serif:wght@400;700&display=swap" rel="stylesheet">
<style>
  :root {
    --page: #e4e2e0;
    --brown: #3d2316;
    --ink: #181818;
    --text: #2a1a12;
    --taupe: #9d8f85;
    --white: #ffffff;
  }
  * { margin: 0; padding: 0; box-sizing: border-box; }
  html, body {
    width: 1200px; height: 900px; overflow: hidden;
    background: var(--page);
    font-family: "Noto Serif", Georgia, serif;
  }
  .card {
    position: absolute; left: 272px;
    width: 626px; height: 359px;
    border-radius: 24px; overflow: hidden;
  }
  .card-front { top: 58px; background: var(--brown); }
  .front-name {
    position: absolute; left: 0; right: 0; top: 192px;
    text-align: center; padding-left: 56px;
    color: var(--white); font-weight: 700; font-size: 35px; letter-spacing: 0.3px;
  }
  .card-back { top: 475px; background: var(--white); }
  .side-strip { position: absolute; left: 0; top: 0; width: 82px; height: 100%; background: var(--ink); }
  .side-band { position: absolute; left: 0; top: 46px; width: 82px; height: 48px; background: var(--brown); }
  .person { position: absolute; left: 97px; top: 44px; color: var(--text); }
  .person-name { font-size: 24px; font-weight: 700; line-height: 1.1; letter-spacing: 0.3px; }
  .person-company { font-size: 12.5px; letter-spacing: 0.4px; margin-top: 1px; }
  .contact-row { position: absolute; left: 0; width: 500px; height: 24px; }
  .contact-icon {
    position: absolute; left: 47px; top: -4px; width: 24px; height: 24px; border-radius: 50%;
    background: var(--white); display: flex; align-items: center; justify-content: center;
  }
  .contact-icon svg { width: 13px; height: 13px; }
  .contact-text { position: absolute; left: 97px; top: 0; font-size: 14.5px; color: var(--text); white-space: nowrap; }
  .brand-name {
    position: absolute; left: 348px; top: 142px; width: 200px;
    text-align: center; color: var(--taupe);
    font-weight: 700; font-size: 22px; letter-spacing: 0.3px; white-space: nowrap;
  }
  .address { position: absolute; left: 379px; top: 264px; font-size: 14.5px; line-height: 1.35; color: var(--text); }
</style>
</head>
<body>
  <section class="card card-front">
    <div class="front-name">Heritage Hollow</div>
  </section>

  <section class="card card-back">
    <div class="side-strip"></div>
    <div class="side-band"></div>

    <div class="person">
      <div class="person-name">MAYA TORVEL</div>
      <div class="person-company">HERITAGE HOLLOW</div>
    </div>

    <div class="brand-name">Heritage Hollow</div>

    <div class="contact-row" style="top:221px">
      <span class="contact-icon">
        <svg viewBox="0 0 16 16"><path fill="#3d2316" d="M3 2h3l1 3-2 1c1 2 2 3 4 4l1-2 3 1v3c0 1-1 2-2 2C6 14 2 10 2 4c0-1 0-2 1-2z"/></svg>
      </span>
      <span class="contact-text">02 6481 7390</span>
    </div>
    <div class="contact-row" style="top:250px">
      <span class="contact-icon">
        <svg viewBox="0 0 16 16"><rect x="1.5" y="3.5" width="13" height="9" fill="#3d2316"/><path d="M1.5 3.5 8 9l6.5-5.5" fill="none" stroke="#fff" stroke-width="1.2"/></svg>
      </span>
      <span class="contact-text">maya@quonbrook.com.au</span>
    </div>
    <div class="contact-row" style="top:279px">
      <span class="contact-icon">
        <svg viewBox="0 0 16 16" fill="none" stroke="#3d2316" stroke-width="1.4"><circle cx="8" cy="8" r="6.3"/><ellipse cx="8" cy="8" rx="2.8" ry="6.3"/><path d="M1.7 8h12.6M3 4.5h10M3 11.5h10"/></svg>
      </span>
      <span class="contact-text">www.heritagehollow.com.au</span>
    </div>

    <div class="address">PO Box Glenwarra<br>NSW 2913</div>
  </section>
</body>
</html>
```